Managed IT Services Business Card + Stationary
Making Technology Work for Your Business
thank you for all the business card submissionns.
I'd like to note a change in the cellphone number to (916) 555-0173
I will try to review the submissions in more detail this evening.

```html
<!DOCTYPE html>
<html lang="en">
<head>
<meta charset="utf-8">
<title>Halvern Managed Services – Business Card</title>
<link rel="stylesheet" href="https://fonts.googleapis.com/css2?family=Exo+2:wght@700&family=Open+Sans:wght@400;600;700&display=swap">
<style>
  :root {
    --page: #f2f2f2;
    --red: #b0141c;
    --ink: #5a5a5a;
    --white: #ffffff;
  }
  * { box-sizing: border-box; margin: 0; padding: 0; }
  html, body { width: 1200px; height: 980px; overflow: hidden; }
  body {
    background: var(--page);
    font-family: "Open Sans", Arial, sans-serif;
    position: relative;
  }
  .card {
    position: absolute;
    left: 200px;
    width: 800px;
    height: 440px;
    border-radius: 26px;
    overflow: hidden;
    box-shadow: 0 6px 18px rgba(0,0,0,0.18);
  }
  .card-back { top: 40px; }
  .card-front { top: 510px; }
  .card svg.card-bg { position: absolute; inset: 0; width: 100%; height: 100%; }

  .back-website {
    position: absolute; left: 40px; top: 34px;
    color: var(--white); font-size: 15px; letter-spacing: 3px; opacity: 0.85;
  }

  .brand {
    position: absolute; left: 250px; top: 92px;
    display: flex; align-items: center; gap: 14px;
  }
  .brand-mark {
    width: 50px; height: 50px; border-radius: 50%;
    background: var(--white);
  }
  .brand-name {
    font-family: "Exo 2", Arial, sans-serif; font-weight: 700;
    font-size: 42px; color: var(--white); letter-spacing: 2px; line-height: 1;
  }
  .brand-tagline {
    font-family: "Exo 2", Arial, sans-serif; font-weight: 700;
    font-size: 13px; color: var(--white); letter-spacing: 6px;
    margin-top: 4px; opacity: 0.85;
  }

  .person {
    position: absolute; right: 390px; top: 258px;
    text-align: right;
    color: var(--ink); font-size: 15px; line-height: 1.45;
  }
  .person-name { font-weight: 700; font-size: 19px; color: var(--red); }
  .person-title { font-weight: 600; }

  .contacts {
    position: absolute; left: 440px; top: 262px;
    list-style: none; color: var(--ink); font-size: 15px;
    padding-left: 22px; border-left: 1px solid #b5b5b5;
  }
  .contacts li { display: flex; align-items: center; gap: 10px; height: 26px; }
  .contact-icon {
    width: 18px; height: 18px; border-radius: 50%;
    background: var(--red); flex: none;
    display: flex; align-items: center; justify-content: center;
  }
  .contact-icon svg { width: 10px; height: 10px; }
</style>
</head>
<body>

<section class="card card-back" aria-label="Card back">
  <svg class="card-bg" viewBox="0 0 800 440" preserveAspectRatio="none">
    <defs>
      <linearGradient id="backRed" x1="0" y1="0" x2="1" y2="1">
        <stop offset="0" stop-color="#c11b22"/>
        <stop offset="1" stop-color="#8a0d13"/>
      </linearGradient>
      <radialGradient id="backOrb" cx="0.4" cy="0.35" r="0.7">
        <stop offset="0" stop-color="#e0464c" stop-opacity="0.7"/>
        <stop offset="1" stop-color="#9a1016" stop-opacity="0.5"/>
      </radialGradient>
    </defs>
    <rect width="800" height="440" fill="url(#backRed)"/>
    <circle class="back-decoration" cx="620" cy="270" r="125" fill="url(#backOrb)"/>
  </svg>
  <p class="back-website">www.halvernms.com</p>
</section>

<section class="card card-front" aria-label="Card front">
  <svg class="card-bg" viewBox="0 0 800 440" preserveAspectRatio="none">
    <defs>
      <linearGradient id="frontSilver" x1="0" y1="0" x2="0" y2="1">
        <stop offset="0" stop-color="#ffffff"/>
        <stop offset="0.5" stop-color="#e6e6e6"/>
        <stop offset="1" stop-color="#bdbdbd"/>
      </linearGradient>
      <linearGradient id="frontRed" x1="0" y1="0" x2="1" y2="1">
        <stop offset="0" stop-color="#c11b22"/>
        <stop offset="1" stop-color="#8a0d13"/>
      </linearGradient>
    </defs>
    <rect width="800" height="440" fill="url(#frontSilver)"/>
    <path d="M0 0 H800 V150 C640 250 380 150 200 200 C120 222 50 230 0 222 Z" fill="#9c9c9c" opacity="0.5"/>
    <path d="M0 0 H800 V140 C640 235 380 140 200 188 C120 210 50 218 0 210 Z" fill="url(#frontRed)"/>
  </svg>

  <div class="brand">
    <span class="brand-mark"></span>
    <div>
      <p class="brand-name">HALVERN</p>
      <p class="brand-tagline">MANAGED SERVICES</p>
    </div>
  </div>

  <div class="person">
    <p class="person-name">Dana Whitlock</p>
    <p class="person-title">Solutions Architect</p>
    <p>1840 Harbor Point Dr.</p>
    <p>Suite #300-214</p>
    <p>Rivermont, CA 95811</p>
  </div>

  <ul class="contacts">
    <li><span class="contact-icon"><svg viewBox="0 0 10 10"><path d="M2 1 L4 1 L4.5 3 L3.4 3.8 C4 5 5 6 6.2 6.6 L7 5.5 L9 6 L9 8 C5 8.5 1.5 5 2 1 Z" fill="#fff"/></svg></span>(916) 555-0142</li>
    <li><span class="contact-icon"><svg viewBox="0 0 10 10"><rect x="3" y="1" width="4" height="8" rx="0.8" fill="#fff"/></svg></span>(916) 555-0173</li>
    <li><span class="contact-icon"><svg viewBox="0 0 10 10"><rect x="1" y="2.5" width="8" height="5" fill="#fff"/><path d="M1 2.5 L5 5.5 L9 2.5" stroke="#b0141c" stroke-width="0.8" fill="none"/></svg></span>dana@halvernms.com</li>
    <li><span class="contact-icon"><svg viewBox="0 0 10 10"><circle cx="5" cy="5" r="3.6" stroke="#fff" stroke-width="1" fill="none"/><path d="M1.4 5 H8.6 M5 1.4 V8.6" stroke="#fff" stroke-width="0.8"/></svg></span>www.halvernms.com</li>
  </ul>
</section>

</body>
</html>
```